a mobile app for beauty salon professional to publish their service and customers to book service

I plan to create an iPhone app (support iPhone 6 and above) that will allow beauty salon professionals (e.g. hair stylist) to publish their service/business with address/geolocation and available time slots, manage their professional profile with photos, and service charges, allow the customers to search services based on locations, and book the service. customer can provide feedback/ratings on the professional's service. a reference website : http://mira.tovelpa.example/booking/

Target Market(s)

beauty and hair salon professionals and customers

Industry/Entity Type

Hair And Beauty

Font styles to use
Sans Serif
Script

Colors

Designer to choose colors to be used in the design.

Requirements
Must have
• === customer features
• - user/customer registration
• - customer browse nearby service using a map view
• - customer browse nearby service using a list view ordered by distance (e.g. km)
• - customer search salon service based on service category, price range, and profressional's rating
• - customer select a service with zoom in details : salon name, service offered, location/address, and a "booking" button
• - customer place booking by specifying service (e.g. simple cut, blow-dry, etc) required, time slot, preferred professional
• - customer payments (paypal/credit card)
• - customer can feedback/rate on the salon professional
• === salon professional features
• - user/professional registration
• - maintain professional profile (private/public), option to upload photos
• - a registered professional can register/maintain shop/business who by default is the owner of the shop/business
• - a shop owner can assign professionals to the shop/business (multiple professional can work in the same location/shop)
• - professional maintain their service and schedule (breaks, holidays, working hours, appointments, service rates)

```html
<!DOCTYPE html>
<html lang="en">
<head>
<meta charset="utf-8">
<title>Mira's Salon — App Screens</title>
<link rel="stylesheet" href="https://fonts.googleapis.com/css2?family=Montserrat:wght@300;400;500;600;700&display=swap">
<style>
:root{
  --pink:#f4589b;
  --pink-soft:#fbd3e4;
  --ink:#1e1e24;
  --grey:#8a8a92;
  --line:#e4e4e8;
  --paper:#ffffff;
  --screen-bg:#fafafa;
  --canvas:#ffffff;
}
*{box-sizing:border-box;margin:0;padding:0}
html,body{width:1200px;height:1200px;overflow:hidden;background:var(--canvas);font-family:"Montserrat",sans-serif;color:var(--ink)}
.canvas{position:relative;width:1200px;height:1200px}
.screen{position:absolute;width:240px;height:426px;border-radius:6px;overflow:hidden;background:var(--screen-bg);box-shadow:0 10px 30px rgba(0,0,0,.12)}
.screen--splash{left:230px;top:50px}
.screen--login{left:730px;top:50px}
.screen--home{left:230px;top:520px}
.screen--schedule{left:730px;top:520px}
.status{position:absolute;top:0;left:0;right:0;height:18px;display:flex;justify-content:space-between;align-items:center;padding:0 8px;font-size:7px;color:var(--pink)}
.status--light{color:rgba(255,255,255,.8)}
.fill{position:absolute;inset:0}
.splash-bg{background:radial-gradient(circle at 55% 45%,#f26a6f 0%,#d444a8 35%,#8a3fd0 65%,#c7a4b8 100%)}
.login-bg{background:linear-gradient(160deg,#2a2d36 0%,#4a3f45 35%,#d9bfb3 65%,#efe3dc 100%)}
.wordmark{position:absolute;left:0;right:0;text-align:center;color:var(--pink);font-weight:600;font-size:30px;letter-spacing:.5px}
.wordmark small{display:block;font-size:12px;font-weight:600;margin-top:2px}
.btn{position:absolute;height:26px;border-radius:2px;background:var(--pink);color:#fff;font-size:9px;font-weight:600;display:flex;align-items:center;justify-content:center;gap:10px}
.btn--ghost{background:transparent;border:1px solid rgba(255,255,255,.8)}
.skip{position:absolute;bottom:30px;left:0;right:0;text-align:center;color:#fff;font-size:9px}
.login-title{position:absolute;top:170px;left:0;right:0;text-align:center;color:#fff;font-size:16px;font-weight:300}
.field{position:absolute;left:26px;right:26px;height:24px;border-bottom:1px solid rgba(255,255,255,.7);display:flex;align-items:center;gap:8px;color:#fff;font-size:9px}
.forgot{position:absolute;right:26px;top:262px;background:var(--pink);color:#fff;font-size:6px;font-weight:600;padding:2px 4px;border-radius:2px}
.social{position:absolute;top:330px;width:26px;height:26px;background:var(--pink);border-radius:2px}
.signup-line{position:absolute;bottom:26px;left:0;right:0;text-align:center;color:#fff;font-size:8px}
.signup-line b{color:var(--pink);text-decoration:underline}
.topbar{position:absolute;top:18px;left:10px;right:10px;height:22px;display:flex;align-items:center;justify-content:space-between;font-size:8px;font-weight:700}
.topbar .loc{flex:1;margin-left:12px}
.topbar .loc span{color:var(--pink)}
.search{position:absolute;top:46px;left:16px;right:16px;height:22px;border:1px solid var(--pink);border-radius:3px;display:flex;align-items:center;gap:6px;padding:0 8px;font-size:7px;color:#b9b9c0}
.tabs{position:absolute;top:78px;left:16px;right:16px;display:flex;justify-content:space-between;font-size:7.5px;color:var(--grey)}
.tabs .active{color:var(--pink);border-bottom:1px solid var(--pink);padding-bottom:3px}
.promo{position:absolute;top:100px;left:0;right:0;height:230px;background:linear-gradient(135deg,#d9a63a 0%,#c18a2c 50%,#3a2a22 100%)}
.promo h2{position:absolute;left:16px;top:70px;font-size:22px;font-weight:300;color:var(--pink)}
.promo p{position:absolute;left:18px;top:100px;font-size:8px;color:#2a1f18}
.tabbar{position:absolute;bottom:0;left:0;right:0;height:44px;background:var(--paper);border-top:1px solid var(--line);display:flex;justify-content:space-around;align-items:center}
.tabbar div{display:flex;flex-direction:column;align-items:center;gap:3px;font-size:6px;font-weight:600}
.tabbar .on{color:var(--pink)}
.sched-title{position:absolute;top:46px;left:0;right:0;text-align:center;color:var(--pink);font-size:14px;font-weight:300}
.label{position:absolute;left:16px;font-size:7.5px;font-weight:700}
.grid{position:absolute;left:16px;right:16px;display:grid;grid-template-columns:repeat(4,1fr);row-gap:12px;font-size:7.5px;text-align:center}
.grid .sel{border:1px solid var(--pink);color:var(--pink);border-radius:2px;padding:2px 0}
.grid span{padding:2px 0}
</style>
</head>
<body>
<main class="canvas">

  <section class="screen screen--splash">
    <div class="fill splash-bg" role="img" aria-label="Soft blurred gradient of violet, magenta and coral light"></div>
    <div class="status status--light"><span>●●●○ FFF</span><span>100%</span></div>
    <div class="wordmark" style="top:130px">Mira's Salon</div>
    <div class="btn" style="left:60px;right:60px;top:230px">Login →</div>
    <div class="btn btn--ghost" style="left:60px;right:60px;top:266px">Sign up →</div>
    <div class="skip">Skip ›</div>
  </section>

  <section class="screen screen--login">
    <div class="fill login-bg" role="img" aria-label="Photograph of a woman with long dark hair touching her hair"></div>
    <div class="status status--light"><span>●●●○ FFF</span><span>100%</span></div>
    <div class="wordmark" style="top:80px">Mira's Salon</div>
    <div class="login-title">Login</div>
    <div class="field" style="top:206px">
      <svg width="10" height="10" viewBox="0 0 10 10"><circle cx="5" cy="3.5" r="2.2" fill="none" stroke="#fff"/><path d="M1 9.5c0-2.2 2-3.3 4-3.3s4 1.1 4 3.3" fill="none" stroke="#fff"/></svg>Email Address</div>
    <div class="field" style="top:236px">
      <svg width="10" height="10" viewBox="0 0 10 10"><rect x="1.5" y="4.5" width="7" height="5" fill="none" stroke="#fff"/><path d="M3 4.5V3a2 2 0 0 1 4 0v1.5" fill="none" stroke="#fff"/></svg>Password</div>
    <div class="forgot">Forgot?</div>
    <div class="btn" style="left:26px;width:110px;top:294px">Login</div>
    <div class="social" style="left:144px" aria-label="Social sign-in"></div>
    <div class="social" style="left:176px" aria-label="Social sign-in"></div>
    <div class="signup-line">Create a new account <b>Signup now</b></div>
  </section>

  <section class="screen screen--home" style="background:var(--paper)">
    <div class="status"><span>●●●○ FFF</span><span>100%</span></div>
    <div class="topbar">
      <svg width="10" height="10" viewBox="0 0 10 10"><circle cx="5" cy="5" r="4.3" fill="none" stroke="#f4589b"/><path d="M6 3L4 5l2 2" fill="none" stroke="#f4589b"/></svg>
      <div class="loc">Melbourn, AU <span>⌄</span></div>
      <svg width="10" height="10" viewBox="0 0 10 10"><path d="M2 7.5h6L7 6V4a2 2 0 0 0-4 0v2z" fill="none" stroke="#f4589b"/><circle cx="8" cy="2" r="1.3" fill="#f4589b"/></svg>
    </div>
    <div class="search"><svg width="9" height="9" viewBox="0 0 9 9"><circle cx="3.8" cy="3.8" r="2.8" fill="none" stroke="#f4589b"/><path d="M6 6l2.5 2.5" stroke="#f4589b"/></svg>Search Salons...</div>
    <div class="tabs"><span class="active">Hair</span><span>Nails</span><span>Waxing</span><span>Massage</span></div>
    <div class="promo" role="img" aria-label="Photograph of a woman pinning up her hair against a golden backdrop">
      <h2>Gift Voucher</h2>
      <p>for the special women</p>
    </div>
    <div class="btn" style="left:26px;width:86px;top:340px">Book now</div>
    <div class="btn" style="left:126px;width:88px;top:340px">Find Stylist</div>
    <nav class="tabbar">
      <div class="on"><svg width="12" height="12" viewBox="0 0 12 12"><path d="M1.5 6L6 2l4.5 4v4.5h-9z" fill="none" stroke="#f4589b"/></svg>Home</div>
      <div><svg width="12" height="12" viewBox="0 0 12 12"><rect x="1.5" y="2.5" width="9" height="8" fill="none" stroke="#1e1e24"/><path d="M1.5 5h9" stroke="#1e1e24"/></svg>Schedule</div>
      <div><svg width="12" height="12" viewBox="0 0 12 12"><circle cx="5" cy="5" r="3.5" fill="none" stroke="#1e1e24"/><path d="M7.5 7.5l3 3" stroke="#1e1e24"/></svg>Search</div>
      <div><svg width="12" height="12" viewBox="0 0 12 12"><path d="M1.5 2.5h7v5h-4l-2 2v-2h-1z" fill="none" stroke="#1e1e24"/></svg>Messages</div>
      <div><svg width="12" height="12" viewBox="0 0 12 12"><circle cx="6" cy="6" r="4.5" fill="none" stroke="#1e1e24"/><circle cx="6" cy="5" r="1.6" fill="none" stroke="#1e1e24"/></svg>Profile</div>
    </nav>
  </section>

  <section class="screen screen--schedule" style="background:var(--paper)">
    <div class="status"><span>●●●○ FFF</span><span>100%</span></div>
    <div class="topbar">
      <svg width="10" height="10" viewBox="0 0 10 10"><circle cx="5" cy="5" r="4.3" fill="none" stroke="#f4589b"/><path d="M6 3L4 5l2 2" fill="none" stroke="#f4589b"/></svg>
      <div class="loc">Melbourn, AU <span>⌄</span></div>
      <svg width="10" height="10" viewBox="0 0 10 10"><path d="M2 7.5h6L7 6V4a2 2 0 0 0-4 0v2z" fill="none" stroke="#f4589b"/><circle cx="8" cy="2" r="1.3" fill="#f4589b"/></svg>
    </div>
    <div class="sched-title">Schedule Time</div>
    <div class="label" style="top:80px">Dates Available</div>
    <div class="grid" style="top:98px">
      <span>15 Mar</span><span class="sel">16 Mar</span><span>17 Mar</span><span>18 Mar</span>
      <span>19 Mar</span><span>20 Mar</span><span>21 Mar</span><span>22 Mar</span>
      <span>23 Mar</span><span>24 Mar</span><span>25 Mar</span><span>26 Mar</span>
    </div>
    <div class="label" style="top:180px">Time Available</div>
    <div class="grid" style="top:198px">
      <span class="sel">9:00</span><span>10:00</span><span>11:00</span><span>12:00</span>
      <span>01:00</span><span>02:00</span><span>03:00</span><span>04:00</span>
      <span>05:00</span><span>06:00</span><span>07:00</span><span>08:00</span>
    </div>
    <div class="btn" style="left:56px;right:56px;top:320px">Review Booking</div>
    <nav class="tabbar">
      <div class="on"><svg width="12" height="12" viewBox="0 0 12 12"><path d="M1.5 6L6 2l4.5 4v4.5h-9z" fill="none" stroke="#f4589b"/></svg>Home</div>
      <div><svg width="12" height="12" viewBox="0 0 12 12"><rect x="1.5" y="2.5" width="9" height="8" fill="none" stroke="#1e1e24"/><path d="M1.5 5h9" stroke="#1e1e24"/></svg>Schedule</div>
      <div><svg width="12" height="12" viewBox="0 0 12 12"><circle cx="5" cy="5" r="3.5" fill="none" stroke="#1e1e24"/><path d="M7.5 7.5l3 3" stroke="#1e1e24"/></svg>Search</div>
      <div><svg width="12" height="12" viewBox="0 0 12 12"><path d="M1.5 2.5h7v5h-4l-2 2v-2h-1z" fill="none" stroke="#1e1e24"/></svg>Messages</div>
      <div><svg width="12" height="12" viewBox="0 0 12 12"><circle cx="6" cy="6" r="4.5" fill="none" stroke="#1e1e24"/><circle cx="6" cy="5" r="1.6" fill="none" stroke="#1e1e24"/></svg>Profile</div>
    </nav>
  </section>

  <div class="wordmark" style="top:990px;font-size:96px;font-weight:600">Mira's Salon</div>

</main>
</body>
</html>
```